Landcape Construction Company needs a flyer to catch attention

A flyer that can be displayed at several different stores detailing our skills, work produced, experience and contact details. Information can be extracted from our website www.brvkw.co.nz. The flyer should feel very green, with addition of pics of work completed as well as stock images of lush green plants, lawns, landscape or similar. Needs to be eye catching with just enough information to express our experience and commitment to high standards

Target Market(s)

Residential
Landscape Architects

Industry/Entity Type

Landscaping

Font styles to use
Serif

Colors
abd037

Requirements
Must have
• Our logo
Experience
Services offered including pictures
All information avail on our website www.brvkw.co.nz
Nice to have
• stock images of lush greenery like a garden after fresh rainfall
Should not have
• Nothing comes to mind

```html
<!DOCTYPE html>
<html lang="en">
<head>
<meta charset="utf-8">
<title>Greenvale Landscape Builders – Flyer</title>
<link rel="stylesheet" href="https://fonts.googleapis.com/css2?family=Montserrat:wght@500;600;700&family=Sorts+Mill+Goudy&family=Libre+Baskerville:wght@700&display=swap">
<style>
  :root{
    --lime:#8dc63f;
    --lime-light:#a4d152;
    --forest:#007a45;
    --forest-deep:#0d6b3c;
    --orange:#f7941d;
    --orange-soft:#fbb766;
    --white:#ffffff;
    --backdrop:#5b5b5b;
  }
  *{box-sizing:border-box;margin:0;padding:0}
  html,body{width:1200px;height:1200px;overflow:hidden}
  body{background:var(--backdrop);position:relative;font-family:"Sorts Mill Goudy",Georgia,serif;color:var(--white)}
  .flyer{position:absolute;top:138px;width:462px;height:924px;overflow:hidden;background:var(--lime)}
  .flyer--front{left:96px}
  .flyer--back{left:642px}
  .flyer svg.art{position:absolute;inset:0;width:462px;height:924px}
  .brand{position:absolute;left:32px;top:38px;display:flex;align-items:center;gap:14px}
  .brand__mark{width:86px;height:86px;border-radius:50%;background:var(--forest)}
  .brand__name{font-family:"Montserrat",Arial,sans-serif;font-weight:600;font-size:19px;line-height:1.2;color:var(--white)}
  .badge{position:absolute;left:239px;top:128px;width:140px;height:160px;text-align:center}
  .badge__stars{font-size:10px;letter-spacing:4px;color:var(--white);line-height:14px}
  .badge__disc{margin:2px auto 0;width:132px;height:132px;border-radius:50%;background:var(--white);display:flex;align-items:center;justify-content:center}
  .badge__inner{width:112px;height:112px;border-radius:50%;background:var(--forest);border:2px solid var(--lime-light);display:flex;flex-direction:column;align-items:center;justify-content:center;font-family:"Montserrat",Arial,sans-serif;font-weight:700;margin-top:-14px}
  .badge__num{font-size:50px;line-height:44px;letter-spacing:-2px}
  .badge__label{font-size:15px;line-height:16px}
  .badge__ribbon{position:absolute;left:-10px;top:110px;width:160px;height:34px;background:var(--orange);border-radius:0 0 50% 50%/0 0 40% 40%;font-family:"Montserrat",Arial,sans-serif;font-weight:700;font-size:19px;line-height:34px;color:var(--white)}
  .headline{position:absolute;left:45px;top:362px;font-family:"Montserrat",Arial,sans-serif}
  .headline__main{font-size:40px;font-weight:600;letter-spacing:1px;line-height:44px}
  .headline__sub{font-size:18.5px;font-weight:500;line-height:22px;margin-top:2px}
  .headline__rule{width:20px;height:3px;background:var(--white);margin-top:12px}
  .service-list{position:absolute;list-style:none}
  .service-list li{display:flex;align-items:center;gap:8px;font-size:21px;white-space:nowrap}
  .service-list svg{width:16px;height:16px;flex:none}
  .service-list--front{left:45px;top:459px}
  .service-list--front li{height:33px}
  .contact-bar{position:absolute;left:42px;top:876px;display:flex;align-items:center;gap:8px;font-family:"Montserrat",Arial,sans-serif;font-weight:500;font-size:22px}
  .contact-bar svg{width:18px;height:18px}
  .contact-bar .gap{width:8px}
  .services-title{position:absolute;left:55px;top:430px;width:351px;height:35px;border:1.5px solid var(--white);border-radius:18px;text-align:center;font-family:"Libre Baskerville",Georgia,serif;font-weight:700;font-size:24px;letter-spacing:12px;line-height:33px;padding-left:12px}
  .service-grid{position:absolute;left:55px;top:484px;display:grid;grid-template-columns:191px auto;row-gap:2px}
  .service-grid .service-list{position:static}
  .service-grid li{height:31px}
  .contact-stack{position:absolute;left:42px;top:812px;list-style:none;font-size:20px}
  .contact-stack li{display:flex;align-items:center;gap:10px;height:29px}
  .contact-stack svg{width:14px;height:14px;flex:none}
  .social{position:absolute;left:332px;top:871px;display:flex;gap:7px}
  .social span{width:20px;height:20px;border-radius:50%;background:#3b5fb0}
  .social span+span{background:#41a9e6}
</style>
</head>
<body>
<svg width="0" height="0" style="position:absolute">
  <defs>
    <symbol id="leaf" viewBox="0 0 16 16">
      <circle cx="8" cy="8" r="6.6" fill="none" stroke="#fff" stroke-width="1"/>
      <path d="M4.5 11 C5 6 8 4.5 11.5 4.5 C11.5 8.5 9 11 4.5 11 Z M4.5 11 L9.5 6.5" fill="none" stroke="#fff" stroke-width="1"/>
    </symbol>
    <symbol id="phone" viewBox="0 0 18 18">
      <circle cx="9" cy="9" r="8" fill="none" stroke="#f7941d" stroke-width="1.5"/>
      <path d="M6 5 L7.5 5 L8.2 7.2 L7.2 8 C7.8 9.4 8.6 10.2 10 10.8 L10.8 9.8 L13 10.5 L13 12 C9 12.5 5.5 9 6 5 Z" fill="#f7941d"/>
    </symbol>
    <symbol id="globe" viewBox="0 0 18 18">
      <circle cx="9" cy="9" r="7.5" fill="none" stroke="#f7941d" stroke-width="1.5"/>
      <ellipse cx="9" cy="9" rx="3.5" ry="7.5" fill="none" stroke="#f7941d" stroke-width="1.2"/>
      <path d="M1.5 9 H16.5 M3 5 H15 M3 13 H15" stroke="#f7941d" stroke-width="1.2"/>
    </symbol>
    <symbol id="mail" viewBox="0 0 18 18">
      <rect x="2" y="4" width="14" height="10" fill="none" stroke="#f7941d" stroke-width="1.5"/>
      <path d="M2 4 L9 10 L16 4" fill="none" stroke="#f7941d" stroke-width="1.5"/>
    </symbol>
    <linearGradient id="lawnGrad" x1="0" y1="0" x2="1" y2="1">
      <stop offset="0" stop-color="#3f8a2a"/>
      <stop offset="0.45" stop-color="#5cb531"/>
      <stop offset="0.8" stop-color="#2f7a2c"/>
      <stop offset="1" stop-color="#9a4c5e"/>
    </linearGradient>
    <linearGradient id="stoneGrad" x1="0" y1="0" x2="0" y2="1">
      <stop offset="0" stop-color="#4f8a2f"/>
      <stop offset="0.35" stop-color="#a9a394"/>
      <stop offset="1" stop-color="#7f7a6e"/>
    </linearGradient>
    <linearGradient id="sprayGrad" x1="0" y1="0" x2="0" y2="1">
      <stop offset="0" stop-color="#c9dcc0"/>
      <stop offset="1" stop-color="#4fa32c"/>
    </linearGradient>
    <linearGradient id="patioGrad" x1="0" y1="0" x2="0" y2="1">
      <stop offset="0" stop-color="#2f3338"/>
      <stop offset="0.5" stop-color="#8f959a"/>
      <stop offset="1" stop-color="#6b7a6a"/>
    </linearGradient>
    <linearGradient id="tileGrad" x1="0" y1="0" x2="0" y2="1">
      <stop offset="0" stop-color="#9fb4c4"/>
      <stop offset="1" stop-color="#8d8f8e"/>
    </linearGradient>
    <linearGradient id="fenceGrad" x1="0" y1="0" x2="1" y2="0">
      <stop offset="0" stop-color="#a7532a"/>
      <stop offset="1" stop-color="#c77a3f"/>
    </linearGradient>
  </defs>
</svg>

<!-- Front flyer -->
<section class="flyer flyer--front">
  <svg class="art" viewBox="0 0 462 924">
    <path role="img" aria-label="Lush green lawn with clipped hedges and pink flowering shrubs" d="M0 172 C90 150 200 178 300 225 C370 200 420 170 462 150 V924 H0 Z" fill="url(#lawnGrad)"/>
    <path d="M0 170 C100 140 210 160 300 215 C370 205 420 175 462 150" fill="none" stroke="#f7941d" stroke-width="11"/>
    <path d="M0 180 C100 155 210 176 300 228 C370 218 420 190 462 168" fill="none" stroke="#fff" stroke-width="6"/>
    <path d="M0 680 C30 710 70 780 130 800 C260 790 380 740 462 700 V730 C370 770 250 820 120 830 C60 820 20 790 0 780 Z" fill="#f7941d"/>
    <path d="M0 780 C30 800 70 825 130 830 C260 820 370 770 462 730 V924 H0 Z" fill="#fff"/>
    <path d="M0 810 C120 820 300 780 462 740 V924 H0 Z" fill="var(--forest)"/>
    <circle cx="130" cy="757" r="100" fill="none" stroke="#fff" stroke-width="1.2"/>
    <circle cx="130" cy="757" r="90" fill="url(#stoneGrad)" role="img" aria-label="Stone block retaining wall topped with a clipped hedge"/>
    <circle cx="273" cy="781" r="80" fill="none" stroke="#fff" stroke-width="1.2"/>
    <circle cx="273" cy="781" r="71" fill="url(#sprayGrad)" role="img" aria-label="Lawn sprinkler spraying water over grass"/>
  </svg>

  <div class="brand">
    <span class="brand__mark"></span>
    <p class="brand__name">Greenvale Landscape<br>Builders Ltd</p>
  </div>

  <div class="badge">
    <div class="badge__stars">★★★★★</div>
    <div class="badge__disc">
      <div class="badge__inner">
        <span class="badge__num">25</span>
        <span class="badge__label">YEARS</span>
      </div>
    </div>
    <div class="badge__ribbon">EXPERIENCE</div>
  </div>

  <div class="headline">
    <p class="headline__main">LOCALLY</p>
    <p class="headline__sub">OWNED AND OPERATED</p>
    <div class="headline__rule"></div>
  </div>

  <ul class="service-list service-list--front">
    <li><svg><use href="#leaf"/></svg>Retaining Walls</li>
    <li><svg><use href="#leaf"/></svg>Gardens &amp; Lawns</li>
    <li><svg><use href="#leaf"/></svg>Irrigation</li>
    <li><svg><use href="#leaf"/></svg>Project Management</li>
    <li><svg><use href="#leaf"/></svg>Consultation</li>
  </ul>

  <div class="contact-bar">
    <svg><use href="#phone"/></svg><span>021 555 0148</span>
    <span class="gap"></span>
    <svg><use href="#globe"/></svg><span>www.brvkw.co.nz</span>
  </div>
</section>

<!-- Back flyer -->
<section class="flyer flyer--back">
  <svg class="art" viewBox="0 0 462 924">
    <rect role="img" aria-label="Modern house with louvred pergola, paved terrace and steps" x="0" y="0" width="462" height="400" fill="url(#patioGrad)"/>
    <path d="M0 300 C40 285 80 300 110 330 C140 370 180 390 230 370 C300 340 360 370 400 320 C430 285 450 270 462 260 V924 H0 Z" fill="var(--lime)"/>
    <circle cx="131" cy="325" r="87" fill="none" stroke="#fff" stroke-width="1.2"/>
    <circle cx="131" cy="325" r="79" fill="url(#patioGrad)" role="img" aria-label="Tiled courtyard with outdoor chairs and hedges"/>
    <path d="M0 740 C80 700 140 700 190 720 L190 740 C130 730 70 740 0 770 Z" fill="#f7941d"/>
    <path d="M0 760 C100 725 200 760 300 770 C380 770 430 770 462 760 V924 H0 Z" fill="var(--forest)"/>
    <path d="M300 812 C380 820 430 816 462 808 V820 C420 826 360 824 300 815 Z" fill="#f7941d"/>
    <circle cx="75" cy="730" r="27" fill="#fff" opacity="0.35"/>
    <circle cx="184" cy="720" r="74" fill="none" stroke="#fff" stroke-width="1.2"/>
    <circle cx="184" cy="720" r="66" fill="url(#tileGrad)" role="img" aria-label="Paved waterfront terrace with hills beyond"/>
    <circle cx="334" cy="751" r="100" fill="none" stroke="#fff" stroke-width="1.2"/>
    <circle cx="334" cy="751" r="91" fill="url(#fenceGrad)" role="img" aria-label="Horizontal slatted timber fence"/>
  </svg>

  <div class="services-title">SERVICES</div>

  <div class="service-grid">
    <ul class="service-list">
      <li><svg><use href="#leaf"/></svg>Patios</li>
      <li><svg><use href="#leaf"/></svg>Paving</li>
      <li><svg><use href="#leaf"/></svg>Concrete</li>
      <li><svg><use href="#leaf"/></svg>Water Features</li>
      <li><svg><use href="#leaf"/></svg>Decking</li>
    </ul>
    <ul class="service-list">
      <li><svg><use href="#leaf"/></svg>Fencing</li>
      <li><svg><use href="#leaf"/></svg>Boardwalks</li>
      <li><svg><use href="#leaf"/></svg>Timber</li>
      <li><svg><use href="#leaf"/></svg>Planter Boxes</li>
      <li><svg><use href="#leaf"/></svg>Planter Boxes</li>
    </ul>
  </div>

  <ul class="contact-stack">
    <li><svg><use href="#mail"/></svg>mark@brvkw.co.nz</li>
    <li><svg><use href="#phone"/></svg>021 555 0148</li>
    <li><svg><use href="#globe"/></svg>www.brvkw.co.nz</li>
  </ul>

  <div class="social"><span></span><span></span></div>
</section>
</body>
</html>
```